12 Week Bright Rally Strong Core Quest Flyer

Hi,
We are a tennis coaching business called Quarry Lane Tennis based in Sydney Australia. We are looking to launch a new 12 week fitness program called "12 Week Bright Rally Core Strong Quest"
We would like the flyer to utilise the colours green and yellow reflecting the tennis theme - however we don't necessarily want it to look like a tennis flyer as tennis is only a small piece of the program via our tennis cardio workouts. We are using tennis cardio as a fitness thing.
We are based in Australia where spring is about to start and everyone is looking to get fit and beach ready for summer so we would like the flyer to communicate fitness, energy, vitality etc. = a Bright Rally Life !
SPECIFICALLY ON THE FLYER WE WOULD LIKE THE FOLLOWING INFO:
Get a Bright Rally Body. Live a Bright Rally Life. In Just 12 Weeks.
Take the challenge today !
Your challenge should you choose to accept it will include:
3 weekly 1hr group training sessions using fast, high intensity & seriously fun cardio workouts. with music to pump you up.
90 Day weight management & nutrition plan using revolutionary nutritional, all natural products. (All products included)
12 Week E-Course covering the dieting dilemma, exercise, stress management and sleep.
Personalised & interactive online membership program which includes:
- Customised meal plans based on your personal nutrition parameters & food preferences
- Step by Step guide to achieving your health goals
- Interactive goal setting charts to track your progress
- Delicious recipe database & thousands of meal options
- Easy interactive nutrition and exercise journal
- Full nutrition support from our team of experts
It's time to take action & get Bright Rally Core Strong !
Only $99 per week !!
Join TODAY
Starts September 17th.
Call 02 8137 2049 or email us at info@quarrylanecourts.example
Please let us know if you need any more info.
Our website is www.quarrylanecourts.example if you want to see more about us but again please keep in mind this is not being marketed as a tennis specific program ... more of a fitness, get ready for summer program.
Thanks
Rosalind
Target Market(s)
Men and women between ages of 27-45 years
Industry/Entity Type
Nutrition
Look and feel

```html
<!DOCTYPE html>
<html lang="en">
<head>
<meta charset="utf-8">
<title>12 Week Bright Rally Strong Core Quest</title>
<link href="https://fonts.googleapis.com/css2?family=Black+Ops+One&family=Architects+Daughter&family=Delius&display=swap" rel="stylesheet">
<style>
  :root {
    --lime: #bfd730;
    --orange: #f26522;
    --yellow: #f5e11a;
    --teal: #6cc6ae;
    --red: #ed1c2e;
    --green: #6abd45;
    --ink: #111111;
    --paper: #ffffff;
  }
  html, body {
    margin: 0;
    padding: 0;
    overflow: hidden;
    background: #ffffff;
  }
  .flyer {
    position: relative;
    width: 1200px;
    height: 927px;
    overflow: hidden;
    color: var(--ink);
    font-family: "Delius", "Comic Sans MS", sans-serif;
  }
  .block { position: absolute; }
  .block--header { left: 0; top: 0; width: 1200px; height: 162px; background: var(--lime); }
  .block--orange { left: 0; top: 162px; width: 659px; height: 486px; background: var(--orange); }
  .block--yellow { left: 659px; top: 162px; width: 209px; height: 765px; background: var(--yellow); }
  .block--teal { left: 868px; top: 162px; width: 332px; height: 421px; background: var(--teal); }
  .block--red { left: 868px; top: 583px; width: 332px; height: 344px; background: var(--red); }
  .block--green { left: 0; top: 648px; width: 659px; height: 279px; background: var(--green); }

  .tagline {
    position: absolute;
    left: 0; top: 14px;
    width: 1200px;
    margin: 0;
    text-align: center;
    font-family: "Black Ops One", "Impact", sans-serif;
    font-weight: 400;
    font-size: 30px;
    line-height: 38px;
    white-space: nowrap;
  }
  .cta-title {
    position: absolute;
    left: 0; top: 70px;
    width: 1200px;
    margin: 0;
    text-align: center;
    font-family: "Black Ops One", "Impact", sans-serif;
    font-weight: 400;
    font-size: 72px;
    letter-spacing: 1px;
    line-height: 1;
    white-space: nowrap;
  }
  .intro {
    position: absolute;
    left: 83px; top: 190px;
    margin: 0;
    font-family: "Architects Daughter", cursive;
    font-size: 28.5px;
    font-weight: 400;
    text-transform: uppercase;
    white-space: nowrap;
  }
  .feature {
    position: absolute;
    left: 14px;
    margin: 0;
    font-size: 24px;
    line-height: 40px;
    white-space: nowrap;
  }
  .feature--training { top: 271px; }
  .feature--nutrition { top: 392px; }
  .feature--course { top: 513px; }
  .feature--membership { top: 595px; }
  .perks {
    position: absolute;
    left: 30px; top: 671px;
    margin: 0;
    padding: 0;
    list-style: none;
    font-size: 25px;
    letter-spacing: 1.4px;
    line-height: 39.6px;
    white-space: nowrap;
  }
  .perks li::before { content: "- "; }

  .closing {
    position: absolute;
    left: 884px; top: 728px;
    width: 304px;
    margin: 0;
    color: var(--paper);
    font-size: 16px;
    line-height: 22px;
  }
  .closing p { margin: 0; }
  .closing__price,
  .closing__join {
    font-family: "Black Ops One", "Impact", sans-serif;
    font-size: 24px;
    line-height: 32px;
    color: var(--ink);
  }
  .closing__start { margin-top: 2px; }
</style>
</head>
<body>
<main class="flyer">
  <div class="block block--header"></div>
  <div class="block block--orange"></div>
  <div class="block block--yellow"></div>
  <div class="block block--teal"></div>
  <div class="block block--red"></div>
  <div class="block block--green"></div>

  <p class="tagline">GET A BRIGHT RALLY BODY. LIVE A BRIGHT RALLY LIFE. IN JUST 12 WEEKS</p>
  <h1 class="cta-title">TAKE THE CHALLENGE TODAY</h1>

  <h2 class="intro">Your challenge should you choose to accept it will include;</h2>

  <p class="feature feature--training">3 weekly 1hr group training sessions using fast, high intensity &amp; seriously fun cardio workouts,<br>with music to pump you up.</p>
  <p class="feature feature--nutrition">90 Day weight management &amp; nutrition plan using revolutionary nutritional, all natural products.<br>(All products included)</p>
  <p class="feature feature--course">12 Week E-Course covering the dieting dilemma, exercise, stress management and sleep.</p>
  <p class="feature feature--membership">Personalised &amp; interactive online membership program which includes:</p>

  <ul class="perks">
    <li>Customised meal plans based on your personal nutrition parameters &amp; food preferences</li>
    <li>Step by Step guide to achieving your health goals</li>
    <li>Interactive goal setting charts to track your progress</li>
    <li>Delicious recipe database &amp; thousands of meal options</li>
    <li>Easy interactive nutrition and exercise journal</li>
    <li>Full nutrition support from our team of experts</li>
  </ul>

  <section class="closing">
    <p class="closing__action">It's time to take action &amp; get<br>Bright Rally Core Strong !</p>
    <p class="closing__price">ONLY $99 PER WEEK !!</p>
    <p class="closing__join">JOIN TODAY</p>
    <p class="closing__start">Starts September 17th.</p>
    <p class="closing__contact">Call 02 8137 2049 or email us at<br>info@quarrylanecourts.example</p>
  </section>
</main>
</body>
</html>
```